Design Brief for Website Redesign

Client Name: Bluecrest IT
Website: www.bluecrestit.com.au
Industry: Managed IT Services
Target Audience: Small to medium-sized businesses in Australia, requiring IT solutions, IT support, cloud services, and phone systems.

Project Overview
We are seeking a full redesign of the Bluecrest IT website to modernize its look, improve usability, and enhance user experience across devices. The goal is to create a professional, clean, and user-friendly website that reflects our expertise in IT services and appeals to our business clients.

Objectives
Modern Visual Identity: Create a fresh, modern design that aligns with Bluecrest IT's branding.

Improved User Experience: Simplify navigation, improve accessibility, and enhance mobile responsiveness.

Clear Calls to Action: Ensure CTAs are prominent and encourage user engagement.

Enhanced Trust & Credibility: Highlight testimonials, case studies, and industry credentials.

SEO Optimization: Ensure the site is optimized for search engines, including proper heading structures and metadata.
Design Style & Tone
Professional: Clean, modern, and polished to reflect our IT expertise.

Minimalist: Simple layouts, plenty of white space, and easy-to-read typography.

Tech-focused: Subtle tech-themed design elements that reinforce our brand as a leading IT service provider.

Colors: Use our existing brand colors, or propose a color scheme that complements the tech industry while maintaining a professional feel.

Typography: Clear, readable fonts that convey professionalism and trustworthiness.

Key Pages & Features
Home Page:

Hero section with a clear value proposition.

Highlight key services (IT support, cloud solutions, phone systems, etc.) with icons and brief descriptions.

Prominent CTAs (e.g., “Request a Quote,” “Book a Demo”).

Testimonials from satisfied clients.

Services Page:

Detailed breakdown of the services we offer (IT support, cloud services, phone systems, etc.).

Use of icons or illustrations to make the services visually engaging.

Clear CTAs to request quotes or book consultations.

About Us Page:

Information about our company history, mission, and team.

Highlight our certifications, partnerships, and industry expertise.

Case Studies/Testimonials Page:

Showcase client success stories and testimonials with visuals and brief case study summaries.

Include a trust-building section with logos of major clients or partners.

Contact Page:

Simple contact form for inquiries.

Integrated map with office location.

Social media links and phone number.

Blog/Resource Section:

Easy-to-navigate blog section for IT-related articles, tips, and industry news.

Clear categorization and tags for easy browsing.

Knowledge Base/Support Page:

Self-service area for clients to find articles, FAQs, and support guides.

Option to submit a support ticket.

Mobile Responsiveness:

Ensure the design is fully responsive, with no horizontal scrolling or misaligned content on mobile.

Functional Requirements
Fast Load Times: Optimize images, minimize unnecessary scripts, and ensure the site loads quickly on both desktop and mobile.

User-Friendly CMS: We need a CMS that is easy to update (preferably WordPress, but open to other suggestions).

SEO Best Practices: Structure the site with proper metadata, alt tags, and semantic HTML for better search engine optimization.

Security: Ensure the website follows security best practices (SSL, HTTPS).

Deliverables
Full website design (desktop and mobile versions).

Design mockups in Photoshop, Sketch, or Figma (whichever is preferred).

Working prototype (optional).

Final website files, including images and assets.

A style guide for ongoing consistency.

Industry/Entity Type

IT Managed Services

Number of Pages Required

3 page

Requirements
Must have
• EXCELLENT UX/UI

```html
<!DOCTYPE html>
<html lang="en">
<head>
<meta charset="utf-8">
<title>Bluecrest IT — Technology Solutions</title>
<link href="https://fonts.googleapis.com/css2?family=Lexend:wght@400;500;600&family=Montserrat:wght@400;500;600;700&family=Dancing+Script:wght@700&display=swap" rel="stylesheet">
<style>
:root{
  --red:#e3202f;
  --navy:#14294a;
  --navy-deep:#0f2443;
  --card:#1a3558;
  --hero:#eef4fc;
  --foot:#e3edf9;
  --ink:#1b2436;
  --muted:#8a93a3;
}
*{margin:0;padding:0;box-sizing:border-box}
html,body{width:1200px;height:2721px;overflow:hidden}
body{position:relative;font-family:"Montserrat",sans-serif;color:var(--ink);background:#fff}
.wordmark{font-family:"Lexend",sans-serif;font-weight:500;color:var(--red);white-space:nowrap}
/* header */
.site-header{position:absolute;left:0;top:0;width:1200px;height:85px;background:#fff}
.site-header .wordmark{position:absolute;left:81px;top:15px;font-size:44px;line-height:54px}
.nav{position:absolute;left:367px;top:36px;display:flex;gap:33px;font-size:13px;font-weight:500;list-style:none}
.nav li.active{color:var(--red);font-weight:700;position:relative}
.nav li.active::before{content:"";position:absolute;left:0;right:0;top:-36px;height:5px;background:var(--red)}
.btn{display:flex;align-items:center;justify-content:center;font-weight:700;font-size:15px;border-radius:6px;text-transform:uppercase}
.btn-contact{position:absolute;left:953px;top:21px;width:152px;height:46px;background:var(--navy);color:#fff}
/* hero */
.hero{position:absolute;left:0;top:85px;width:1200px;height:558px;background:var(--hero)}
.hero h1{position:absolute;left:112px;top:85px;font-family:"Lexend",sans-serif;font-weight:600;font-size:45px;line-height:54px;color:var(--navy)}
.hero p{position:absolute;left:112px;top:215px;width:470px;font-size:15px;line-height:29px}
.hero .tag{position:absolute;left:198px;top:322px;font-family:"Dancing Script",cursive;font-size:21px}
.btn-quote{position:absolute;left:112px;top:369px;width:196px;height:47px;background:var(--red);color:#fff}
.btn-demo{position:absolute;left:335px;top:369px;width:196px;height:47px;background:var(--navy);color:#fff}
.hero-art{position:absolute;left:605px;top:75px;width:590px;height:355px;border-radius:20px;background:radial-gradient(ellipse at 55% 55%,#dfe7f3,#eef4fc 70%)}
.rule{position:absolute;left:112px;width:978px;height:2px;background:#d6dbe3}
/* clients */
.clients-title{position:absolute;left:26px;top:700px;font-family:"Lexend",sans-serif;font-weight:500;font-size:23px;line-height:30px;color:var(--navy)}
.client{position:absolute;top:716px;font-family:"Lexend",sans-serif;font-weight:600;font-size:24px;color:var(--navy);display:flex;align-items:center;gap:8px}
.client .dot{width:22px;height:22px;border-radius:50%;background:#2a8fd8}
/* services */
.services{position:absolute;left:0;top:825px;width:1200px;height:759px;background:radial-gradient(ellipse at 25% 20%,#1d3a62,var(--navy-deep) 70%);overflow:hidden}
.services .kicker{position:absolute;left:112px;top:92px;font-family:"Lexend",sans-serif;font-size:23px;font-weight:500;color:#fff}
.services h2{position:absolute;left:112px;top:130px;font-family:"Lexend",sans-serif;font-weight:600;font-size:41px;line-height:48px;color:#fff}
.arrow-btn{position:absolute;width:44px;height:44px;border-radius:50%;border:2px solid #fff;display:flex;align-items:center;justify-content:center}
.svc{position:absolute;top:266px;width:296px;height:380px;background:var(--card);color:#fff}
.svc.featured{background:linear-gradient(150deg,#e8202f,#d81a2a)}
.svc svg{position:absolute;left:29px;top:32px}
.svc h3{position:absolute;left:30px;top:136px;font-family:"Lexend",sans-serif;font-weight:400;font-size:23px;white-space:nowrap}
.svc p{position:absolute;left:28px;top:182px;width:250px;font-size:15px;line-height:28.5px}
.svc .read{position:absolute;left:19px;top:282px;width:257px;height:49px;border:1px solid #fff;border-radius:6px;display:flex;align-items:center;justify-content:center;font-weight:700;font-size:15px}
.svc.featured .read{background:#fff;color:var(--red)}
/* testimonials */
.testi-kicker{position:absolute;left:0;width:1200px;top:1667px;text-align:center;font-family:"Lexend",sans-serif;font-weight:500;font-size:22px}
.testi-title{position:absolute;left:0;width:1200px;top:1705px;text-align:center;font-family:"Lexend",sans-serif;font-weight:600;font-size:42px;color:var(--navy)}
.frame{position:absolute;border:2px solid var(--red);border-radius:4px}
.tcard{position:absolute;background:#fff;box-shadow:0 4px 18px rgba(20,41,74,.12);overflow:hidden}
.quote{position:absolute;font-family:"Lexend",sans-serif;font-weight:600;font-size:100px;line-height:1;color:var(--red);background:#fff;padding:0 6px}
.tcard .client-name{position:absolute;left:32px;top:36px;font-family:"Lexend",sans-serif;font-weight:600;font-size:26px;color:var(--navy)}
.tcard .person{position:absolute;left:224px;top:28px;font-size:21px;color:var(--red)}
.tcard .role{position:absolute;left:224px;top:63px;font-size:17px}
.tcard .body{position:absolute;left:32px;top:120px;width:700px;font-size:16px;line-height:29px}
/* footer */
.footer{position:absolute;left:0;top:2210px;width:1200px;height:511px;background:var(--foot)}
.footer .wordmark{position:absolute;left:118px;top:80px;font-size:50px;line-height:60px}
.social{position:absolute;top:212px;width:50px;height:50px;border-radius:50%;background:var(--navy)}
.fcol{position:absolute;top:85px}
.fcol h4{font-family:"Lexend",sans-serif;font-weight:500;font-size:19px;color:var(--navy);margin-bottom:14px}
.fcol ul{list-style:none}
.fcol li{font-size:15px;height:34.3px;display:flex;align-items:flex-start;gap:9px;white-space:nowrap}
.fcol li::before{content:"➜";font-size:13px;color:var(--navy)}
.copy{position:absolute;left:0;width:1200px;top:2660px;text-align:center;font-size:14px}
</style>
</head>
<body>

<header class="site-header">
  <div class="wordmark">Bluecrest</div>
  <ul class="nav">
    <li class="active">HOME</li><li>SERVICES</li><li>ABOUT US</li><li>TESTIMONIALS</li><li>BLOG</li><li>SUPPORT</li>
  </ul>
  <a class="btn btn-contact">Contact Us</a>
</header>

<section class="hero">
  <h1>Technology Solutions<br>for a better business</h1>
  <p>We understand that technology is a critical component of running a successful business, and that's why we're here to help you navigate the ever-changing landscape of IT.</p>
  <div class="tag">Looking for Office IT Support?</div>
  <a class="btn btn-quote">Request a Quote</a>
  <a class="btn btn-demo">Book a Demo</a>
  <div class="hero-art" role="img" aria-label="Illustration of a person with a laptop riding a rocket surrounded by tech icons"></div>
</section>
<div class="rule" style="top:642px"></div>

<h3 class="clients-title">Some customers<br>we support</h3>
<div class="client" style="left:249px">Summitview</div>
<div class="client" style="left:433px"><span class="dot"></span>Harbourline</div>
<div class="client" style="left:683px;background:#111;color:#fff;padding:4px 12px;font-weight:400">Kestrel Property</div>
<div class="client" style="left:941px;color:#2a8fd8;font-size:32px;font-weight:500;top:712px">Marlowe &amp; Co</div>

<section class="services">
  <div class="kicker">key services</div>
  <h2>IT support, cloud solutions,<br>phone systems, etc.</h2>
  <div class="arrow-btn" style="left:972px;top:160px;border-color:#9fb0c6"><svg width="20" height="20" viewBox="0 0 20 20"><path d="M17 10H3M9 4L3 10l6 6" stroke="#9fb0c6" stroke-width="2" fill="none"/></svg></div>
  <div class="arrow-btn" style="left:1041px;top:160px"><svg width="20" height="20" viewBox="0 0 20 20"><path d="M3 10h14M11 4l6 6-6 6" stroke="#fff" stroke-width="2" fill="none"/></svg></div>

  <div class="svc" style="left:112px">
    <svg width="70" height="70" viewBox="0 0 70 70" fill="none" stroke="#fff" stroke-width="2"><circle cx="38" cy="34" r="9"/><path d="M34 44h8M35 48h6M5 58l12-8h14l10 6H22M10 8v10M18 4v14M26 10v8M56 40a6 6 0 1 0 .1 0"/></svg>
    <h3>IT solutions</h3>
    <p>Make the most of technology with expert advice and guidance on IT best practices.</p>
    <div class="read">READ MORE</div>
  </div>
  <div class="svc featured" style="left:429px">
    <svg width="70" height="70" viewBox="0 0 70 70" fill="none" stroke="#fff" stroke-width="2"><circle cx="35" cy="14" r="7"/><path d="M20 30h30v10a15 15 0 0 1-30 0zM12 34h8M50 34h8M24 24l-6-6M46 24l6-6M28 58h14"/></svg>
    <h3>IT support</h3>
    <p>Our certified systems engineers have deep expertise and experience</p>
    <div class="read">READ MORE</div>
  </div>
  <div class="svc" style="left:747px">
    <svg width="70" height="70" viewBox="0 0 70 70" fill="none" stroke="#fff" stroke-width="2"><rect x="30" y="4" width="34" height="44" rx="2"/><path d="M36 14h22M36 22h22M36 30h22M12 8v22M6 24l6 6 6-6M4 58a10 10 0 0 1 10-14 12 12 0 0 1 22 4h-32z"/><circle cx="52" cy="56" r="7"/></svg>
    <h3>Cloud services</h3>
    <p>Make the most of technology with expert advice and guidance on IT best practices.</p>
    <div class="read">READ MORE</div>
  </div>
  <div class="svc" style="left:1065px">
    <svg width="70" height="70" viewBox="0 0 70 70" fill="none" stroke="#fff" stroke-width="2"><path d="M12 8h40a6 6 0 0 1 6 6v4H6v-4a6 6 0 0 1 6-6zM20 18v12h24V18M32 30v10M14 40h36M14 40v8M32 40v8M50 40v8"/><circle cx="14" cy="54" r="4"/><circle cx="32" cy="54" r="4"/><circle cx="50" cy="54" r="4"/></svg>
    <h3>Phone systems</h3>
    <p>Modern cloud phones and chat-based calling for the modern office.</p>
    <div class="read">READ MORE</div>
  </div>
</section>

<div class="testi-kicker">Testimonials</div>
<h2 class="testi-title">What Our Clients Say</h2>

<div class="frame" style="left:-20px;top:1830px;width:107px;height:266px"></div>
<div class="tcard" style="left:-20px;top:1850px;width:131px;height:262px">
  <div class="body" style="left:20px;top:120px;width:110px;color:var(--muted)">siness.<br>We</div>
</div>
<div class="frame" style="left:1087px;top:1825px;width:140px;height:264px"></div>
<div class="quote" style="left:1150px;top:1780px">“</div>
<div class="tcard" style="left:1114px;top:1845px;width:120px;height:262px">
  <div class="client-name" style="left:32px;top:40px"><span style="display:inline-block;width:22px;height:22px;border-radius:50%;background:#2a8fd8"></span></div>
  <div class="body" style="color:var(--muted);width:90px;white-space:nowrap">I wish t<br>The se<br>would</div>
</div>

<div class="frame" style="left:196px;top:1825px;width:778px;height:264px"></div>
<div class="quote" style="left:258px;top:1780px">“</div>
<div class="tcard" style="left:223px;top:1845px;width:775px;height:262px">
  <div class="client-name">Summitview</div>
  <div class="person">Dana Morell</div>
  <div class="role">Principal/Senior Property Manager</div>
  <div class="body">I wish to thank Bluecrest IT for their outstanding services &amp; for looking after our business. The services they provide make the daily operation of our business very smooth. We would have not survived without them.</div>
</div>
<div class="arrow-btn" style="left:125px;top:1939px;border-color:#c5ccd6"><svg width="20" height="20" viewBox="0 0 20 20"><path d="M17 10H3M9 4L3 10l6 6" stroke="#c5ccd6" stroke-width="2" fill="none"/></svg></div>
<div class="arrow-btn" style="left:1022px;top:1940px;background:var(--red);border-color:var(--red);width:40px;height:40px"><svg width="20" height="20" viewBox="0 0 20 20"><path d="M3 10h14M11 4l6 6-6 6" stroke="#fff" stroke-width="2" fill="none"/></svg></div>

<footer class="footer">
  <div class="wordmark">Bluecrest</div>
  <div class="social" style="left:138px" role="img" aria-label="Social profile"></div>
  <div class="social" style="left:214px" role="img" aria-label="Social profile"></div>
  <div class="social" style="left:290px" role="img" aria-label="Social profile"></div>
  <div class="fcol" style="left:429px"><h4>ABOUT US</h4><ul><li>Our Company</li><li>Our Team</li><li>Bluecrest IT Partners</li><li>Contact Us</li></ul></div>
  <div class="fcol" style="left:633px"><h4>USEFUL LINKS</h4><ul><li>Services</li><li>Blog</li><li>Videos</li><li>Crestline Meet</li></ul></div>
  <div class="fcol" style="left:856px"><h4>OUR SOLUTIONS</h4><ul><li>IT Support</li><li>Project Management</li><li>IT Consulting and Training</li><li>Hardware and Software</li><li>IT Cyber Security</li><li>Cloud Solutions</li><li>IT Procurement and Auditing</li><li>Mobile and Web Development</li></ul></div>
</footer>
<div class="rule" style="top:2624px;background:#b9c2cf"></div>
<div class="copy">© 2025 Bluecrest I All Rights Reserved</div>

</body>
</html>
```